Need a banner designed to help prank my neighbor.

I'm looking for creativity and fun in a banner that I will hang on a large tree outside my house facing a neighbor. He just started decorating for Christmas and I always joke with him that it is too early. This is a fun project. Nothing too serious. I welcome your skills to make it awesome.

I have the basics of a sign designed (attached), but I need it brought to the next level with better font and images.

Banner will be printed at 4-feet x 8-feet.
Top part of my mock up is most important to see/read easily.

```html
<!DOCTYPE html>
<html lang="en">
<head>
<meta charset="utf-8">
<title>Thanksgiving First Banner</title>
<link rel="stylesheet" href="https://fonts.googleapis.com/css2?family=Montserrat:wght@600;800;900&display=swap">
<style>
  :root {
    --page-bg: #efeeee;
    --banner-center: #e9b622;
    --banner-edge: #d5842b;
    --ink: #0a0a0a;
    --ribbon-red: #ad1f24;
    --paper-white: #ffffff;
    --jacket-red: #b3262a;
    --shirt-cream: #efe4c4;
  }
  html, body {
    margin: 0;
    padding: 0;
    width: 1200px;
    height: 1200px;
    overflow: hidden;
    background: var(--page-bg);
  }
  .canvas {
    position: relative;
    width: 1200px;
    height: 1200px;
  }
  .banner {
    position: absolute;
    left: 40px;
    top: 320px;
    width: 1120px;
    height: 560px;
    display: block;
  }
  .headline {
    font-family: "Montserrat", sans-serif;
    font-weight: 900;
    fill: var(--ink);
  }
  .ribbon-text {
    font-family: "Montserrat", sans-serif;
    font-weight: 900;
    fill: var(--paper-white);
  }
  .subhead {
    font-family: "Montserrat", sans-serif;
    font-weight: 900;
    fill: var(--ink);
  }
  .hashtag {
    font-family: "Montserrat", sans-serif;
    font-weight: 600;
    fill: var(--ink);
  }
</style>
</head>
<body>
<main class="canvas">
  <svg class="banner" viewBox="0 0 1120 560" xmlns="http://www.w3.org/2000/svg" aria-label="Stop premature Christmas decorating banner">
    <defs>
      <radialGradient id="banner-glow" cx="50%" cy="50%" r="65%">
        <stop offset="0%" stop-color="var(--banner-center)"/>
        <stop offset="100%" stop-color="var(--banner-edge)"/>
      </radialGradient>
      <linearGradient id="figure-tones" x1="0" y1="0" x2="0" y2="1">
        <stop offset="0%" stop-color="#9c6b45"/>
        <stop offset="45%" stop-color="var(--jacket-red)"/>
        <stop offset="100%" stop-color="var(--shirt-cream)"/>
      </linearGradient>
    </defs>

    <rect class="banner-field" x="0" y="0" width="1120" height="560" fill="url(#banner-glow)"/>

    <rect class="figure-illustration" role="img"
          aria-label="Illustration of a bearded man in a red jacket covering his eyes with one hand and raising the other palm in a stop gesture"
          x="318" y="66" width="520" height="238" rx="18"
          fill="url(#figure-tones)" opacity="0.85"/>

    <text class="headline" x="128" y="290" font-size="292" textLength="870" lengthAdjust="spacingAndGlyphs">STOP</text>

    <rect class="ribbon" x="84" y="304" width="949" height="77" fill="var(--ribbon-red)"/>
    <text class="ribbon-text" x="111" y="360" font-size="48" textLength="907" lengthAdjust="spacingAndGlyphs">PREMATURE CHRISTMAS DECORATING.</text>

    <text class="subhead" x="560" y="455" font-size="55" text-anchor="middle" textLength="618" lengthAdjust="spacingAndGlyphs">THANKSGIVING FIRST.</text>

    <text class="hashtag" x="72" y="500" font-size="26" textLength="376" lengthAdjust="spacingAndGlyphs">#lightsgoupafterthanksgiving</text>
    <text class="hashtag" x="483" y="500" font-size="26" textLength="284" lengthAdjust="spacingAndGlyphs">#savethebabyreindeer</text>
    <text class="hashtag" x="805" y="500" font-size="26" textLength="242" lengthAdjust="spacingAndGlyphs">#lookingatyou3170</text>
  </svg>
</main>
</body>
</html>
```